Corporate consulting business needs a business card

I want a professional business card.... surprise me

Updates

Reason: i dont think 2 days is enough

Target Market(s)

Corprorate and Not for Profit firms and organisations

Industry/Entity Type

Consulting

Contact Information for Business Card

Logo
Corporate Consulting Services
On Time, On Budget, Beyond Expectation
Tovan Presfield
Director
0427 31 94 62 (Larger)
tovan@tp-advisory.com.au
www.tp-advisory.com.au
include little icons beside the contact info:

- Envelope = email
- Phone = phone
- Globe = website

Font styles to use
Serif
Sans Serif

Requirements
Must have
• Professional and clean
Nice to have
• you tell me

```html
<!DOCTYPE html>
<html lang="en">
<head>
<meta charset="utf-8">
<title>TP Advisory Services – Business Card</title>
<link rel="stylesheet" href="https://fonts.googleapis.com/css2?family=Libre+Baskerville:wght@700&family=Open+Sans:wght@400;700&display=swap">
<style>
  :root {
    --bg: #e4e4e2;
    --brown: #4a2c1c;
    --brown-deep: #1e0f08;
    --brown-dark: #2c170d;
    --black: #0d0d0d;
    --white: #ffffff;
    --ink: #1a1a1a;
    --serif: "Libre Baskerville", Georgia, serif;
    --sans: "Open Sans", Arial, sans-serif;
  }
  * { margin: 0; padding: 0; box-sizing: border-box; }
  html, body { width: 1200px; height: 900px; overflow: hidden; }
  body { background: var(--bg); position: relative; font-family: var(--sans); }

  .card {
    position: absolute;
    width: 560px;
    height: 320px;
    overflow: hidden;
    box-shadow: 0 10px 26px rgba(0,0,0,.22);
  }

  /* Back side */
  .card-back {
    left: 90px; top: 80px;
    background: linear-gradient(135deg, var(--brown-dark) 0%, var(--brown-deep) 70%, #120804 100%);
    color: var(--white);
  }
  .card-back .brand { position: absolute; left: 0; right: 0; top: 104px; }
  .card-back .web-row {
    position: absolute; left: 0; right: 0; top: 236px;
    display: flex; align-items: center; justify-content: center; gap: 14px;
    font-size: 15px; letter-spacing: .2px;
  }
  .web-row .rule { height: 2px; width: 120px; background: linear-gradient(90deg, transparent, var(--white)); }
  .web-row .rule.right { background: linear-gradient(90deg, var(--white), transparent); }

  /* Brand lockup */
  .brand { display: flex; align-items: center; justify-content: center; gap: 14px; }
  .brand-dot {
    width: 44px; height: 44px; border-radius: 50%;
    border: 3px solid currentColor;
  }
  .brand-name {
    font-family: var(--serif); font-weight: 700;
    font-size: 22px; letter-spacing: .5px; text-transform: uppercase;
  }

  /* Front side */
  .card-front {
    left: 550px; top: 490px;
    background: var(--white);
    color: var(--ink);
  }
  .card-front .brand { position: absolute; left: 40px; right: 40px; top: 50px; color: var(--ink); }
  .card-front .brand-name { font-size: 20px; }

  .contact-band {
    position: absolute; left: 300px; top: 125px; width: 260px; height: 110px;
    background: var(--brown);
    color: var(--white);
    padding: 18px 0 0 38px;
  }
  .contact-band::before {
    content: ""; position: absolute; left: -1px; top: 44px;
    border-style: solid; border-width: 9px 0 9px 9px;
    border-color: transparent transparent transparent var(--white);
  }
  .contact-list { list-style: none; font-size: 13px; line-height: 1; }
  .contact-list li { display: flex; align-items: center; gap: 9px; margin-bottom: 8px; }
  .contact-list .phone-number { font-size: 15px; }
  .contact-list svg { width: 14px; height: 14px; flex: none; fill: var(--white); }

  .name-band {
    position: absolute; left: 0; top: 196px; width: 300px; height: 92px;
    background: var(--black);
    color: var(--white);
    text-align: center;
    padding-top: 20px;
  }
  .name-band::before {
    content: ""; position: absolute; left: 136px; top: 0;
    border-style: solid; border-width: 9px 9px 0 9px;
    border-color: var(--white) transparent transparent transparent;
  }
  .person-name { font-weight: 700; font-size: 20px; letter-spacing: -.2px; }
  .person-title { font-size: 15px; margin-top: 2px; }
</style>
</head>
<body>

<section class="card card-back" aria-label="Business card, back">
  <div class="brand">
    <span class="brand-dot" aria-hidden="true"></span>
    <span class="brand-name">TP Advisory Services</span>
  </div>
  <div class="web-row">
    <span class="rule"></span>
    <span class="web-address">www.tp-advisory.com.au</span>
    <span class="rule right"></span>
  </div>
</section>

<section class="card card-front" aria-label="Business card, front">
  <div class="brand">
    <span class="brand-dot" aria-hidden="true"></span>
    <span class="brand-name">TP Advisory Services</span>
  </div>

  <div class="contact-band">
    <ul class="contact-list">
      <li class="phone-number">
        <svg viewBox="0 0 24 24" aria-hidden="true"><path d="M6.6 10.8c1.4 2.8 3.8 5.1 6.6 6.6l2.2-2.2c.3-.3.7-.4 1-.2 1.1.4 2.3.6 3.6.6.6 0 1 .4 1 1V20c0 .6-.4 1-1 1C10.6 21 3 13.4 3 4c0-.6.4-1 1-1h3.5c.6 0 1 .4 1 1 0 1.3.2 2.5.6 3.6.1.3 0 .7-.2 1l-2.3 2.2z"/></svg>
        <span>0427 31 94 62</span>
      </li>
      <li>
        <svg viewBox="0 0 24 24" aria-hidden="true"><path d="M3 5h18c.6 0 1 .4 1 1v12c0 .6-.4 1-1 1H3c-.6 0-1-.4-1-1V6c0-.6.4-1 1-1zm1 2.2V17h16V7.2l-8 5.3-8-5.3zM5.2 7 12 11.5 18.8 7H5.2z"/></svg>
        <span>tovan@tp-advisory.com.au</span>
      </li>
      <li>
        <svg viewBox="0 0 24 24" aria-hidden="true"><path d="M12 2a10 10 0 1 0 0 20 10 10 0 0 0 0-20zm6.9 6h-2.9a15.7 15.7 0 0 0-1.4-3.6A8 8 0 0 1 18.9 8zM12 4c.8 1.2 1.5 2.5 1.9 4h-3.8c.4-1.5 1.1-2.8 1.9-4zM4.3 14a8.2 8.2 0 0 1 0-4h3.4a16 16 0 0 0 0 4H4.3zm.8 2h2.9c.3 1.3.8 2.5 1.4 3.6A8 8 0 0 1 5.1 16zM8 8H5.1a8 8 0 0 1 4.3-3.6C8.8 5.5 8.3 6.7 8 8zm4 12c-.8-1.2-1.5-2.5-1.9-4h3.8c-.4 1.5-1.1 2.8-1.9 4zm2.3-6H9.7a14.7 14.7 0 0 1 0-4h4.6a14.7 14.7 0 0 1 0 4zm.3 5.6c.6-1.1 1.1-2.3 1.4-3.6h2.9a8 8 0 0 1-4.3 3.6zM16.3 14a16 16 0 0 0 0-4h3.4a8.2 8.2 0 0 1 0 4h-3.4z"/></svg>
        <span>www.tp-advisory.com.au</span>
      </li>
    </ul>
  </div>

  <div class="name-band">
    <p class="person-name">Tovan Presfield</p>
    <p class="person-title">Director</p>
  </div>
</section>

</body>
</html>
```